Single Page Production Company Site

Clean. Simple. Minimalist site with one page.

No portfolio, just some text to communicate a general overview of what the company does.

We work for a very select group of clients, creating strong brand personalities online. The site is specifically minimal and not communicating too much about what we do.. we have a variety of capabilities to work with clients and prefer to be broad with just a simple landing page as the point of contact for our brand.
Updates

Christmas holidays are coming up, maybe people need some time away from work with family and friends... We can keep working on this and I will provide feedback as quickly as possible, but I understand if designers have other commitments during the coming days. Thanks for your hard work!

Industry/Entity Type

Design Agency

Coding

Coded - Design and coding required

Number of Pages Required

1 page

Font styles to use
Sans Serif

Requirements
Must have
• Clean, bold text headlines.
Nice to have
• Unsure about any images used in the design, would like to see options with or without.

```html
<!DOCTYPE html>
<html lang="en">
<head>
<meta charset="utf-8">
<title>Cedars Development Co.</title>
<link href="https://fonts.googleapis.com/css2?family=Roboto:wght@400;500;700;900&display=swap" rel="stylesheet">
<style>
:root{
  --brown-dark:#3d2a24;
  --brown:#4a342d;
  --brown-mid:#5a443c;
  --white:#ffffff;
  --text:#2b2b2b;
  --muted:#555;
  --rule:#9a9a9a;
  --accent:#e07a52;
  --field:#e4e4e4;
}
*{box-sizing:border-box;margin:0;padding:0}
html,body{width:1200px;height:2535px;overflow:hidden}
body{font-family:'Roboto',Arial,sans-serif;color:var(--text);background:var(--white);position:relative}
section,header,footer,.topbar{position:absolute;left:0;width:1200px}
.abs{position:absolute}

.topbar{top:0;height:34px;background:var(--brown-dark);color:var(--white);font-size:10px;font-weight:700}
.topbar .contact{left:172px;top:0;height:34px;display:flex;align-items:center;gap:26px}
.topbar .contact span{display:flex;align-items:center;gap:8px}
.topbar .nav{right:172px;top:0;height:34px;display:flex;align-items:center;gap:20px}

.site-header{top:34px;height:73px;background:var(--white)}
.brand{left:172px;top:10px;display:flex;align-items:baseline;gap:4px;color:var(--brown-dark)}
.brand-name{font-size:40px;font-weight:900;letter-spacing:.5px}
.brand-sub{font-size:9px;font-weight:500}
.menu-btn{left:893px;top:23px;width:29px;height:24px;border:2px solid var(--brown-dark);border-radius:4px;display:flex;align-items:center;justify-content:center}
.btn{display:inline-flex;align-items:center;justify-content:center;border-radius:20px;font-size:10px;font-weight:700;text-transform:uppercase}
.btn-dark{background:var(--brown-dark);color:var(--white)}
.btn-light{background:#eeeeee;color:var(--brown-dark)}
.header-cta{left:938px;top:17px;width:91px;height:34px}

.hero{top:107px;height:515px;background:linear-gradient(90deg,#f3eee6 0%,#e9e1d2 35%,#cbb9a1 60%,#8e7866 80%,#c9bda9 100%)}
.hero-photo{inset:0}
.hero-rule{left:172px;top:191px;width:68px;height:2px;background:var(--brown-dark)}
.hero-title{left:172px;top:200px;font-size:45px;font-weight:900;color:var(--brown-dark)}
.hero-sub{left:172px;top:253px;font-size:20px;color:var(--brown-dark)}
.hero-btn{left:172px;top:307px;width:94px;height:31px}
.hero-arrow{left:30px;top:244px;width:36px;height:36px;border-radius:50%;background:#c9c4bd;display:flex;align-items:center;justify-content:center}

.section-label{width:100%;text-align:center;font-size:11px;font-weight:700;text-transform:uppercase;color:var(--text)}
.section-title{width:100%;display:flex;align-items:center;justify-content:center;gap:12px;font-size:46px;font-weight:900;color:var(--brown-dark);text-transform:uppercase}
.section-title::before,.section-title::after{content:"";width:170px;height:4px;background:var(--rule)}

.services{top:622px;height:323px}
.services .section-label{top:54px}
.services .section-title{top:66px}
.service-card{top:141px;width:273px;height:144px;border:2px solid var(--brown-dark);padding:18px 16px;text-align:center}
.service-card h3{font-size:15px;font-weight:900;text-transform:uppercase;color:var(--text);margin-bottom:18px}
.service-card p{font-size:11px;line-height:17px;text-align:justify;text-align-last:center;color:var(--muted)}

.team{top:945px;height:535px;background:linear-gradient(135deg,#4b3730 0%,#5e4840 45%,#4a352e 100%);color:var(--white)}
.team-label{left:172px;top:56px;font-size:11px;font-weight:700}
.team-title{left:172px;top:66px;display:flex;align-items:center;gap:10px;font-size:46px;font-weight:900}
.team-title::after{content:"";width:170px;height:3px;background:#8f8681}
.team-intro{left:172px;top:122px;font-size:11px}
.member{top:177px;width:273px}
.member-photo{width:273px;height:140px;border:2px solid var(--accent)}
.member h3{font-size:13px;font-weight:900;text-transform:uppercase;margin:12px 0 10px}
.member p{font-size:11px;line-height:14px;text-align:justify;height:58px}
.member .btn{width:93px;height:31px;margin-top:20px}

.approach{top:1480px;height:440px}
.approach .section-label{top:46px}
.approach .section-title{top:58px}
.approach-sub{top:120px;width:100%;text-align:center;font-size:11px;color:var(--muted)}
.approach-copy{left:172px;top:173px;width:388px;font-size:11px;line-height:19px;color:var(--muted)}
.approach-copy strong{display:block;margin-top:16px;font-size:12px;line-height:20px;color:var(--text);font-weight:700}
.approach-btn{left:172px;top:338px;width:94px;height:31px}
.approach-photo{left:590px;top:175px;width:439px;height:198px;background:linear-gradient(90deg,#8d7a55 0%,#c9b98d 35%,#6d6a66 65%,#3c3a36 100%)}

.contact{top:1920px;height:500px;background:linear-gradient(160deg,#4a362f 0%,#5a453d 50%,#46322b 100%);color:var(--white);text-align:center}
.contact-kicker{top:40px;width:100%;font-size:34px;font-weight:700}
.contact-title{top:76px;width:100%;font-size:92px;font-weight:900;line-height:1}
.field{background:var(--field);color:#8a8a8a;font-size:11px;padding:0 22px;display:flex;align-items:center;text-transform:uppercase;height:38px}
.field-name{left:160px;top:215px;width:342px}
.field-email{left:512px;top:215px;width:256px}
.field-phone{left:779px;top:215px;width:257px}
.field-message{left:160px;top:263px;width:876px;height:89px;align-items:flex-start;padding-top:16px}
.submit{left:550px;top:390px;width:135px;height:42px;border:3px solid #c9c9c9;border-radius:22px;background:#f1f1f1;color:var(--brown-dark);font-size:19px;font-weight:900;display:flex;align-items:center;justify-content:center}

.site-footer{top:2420px;height:115px;background:var(--brown-dark);color:var(--white);text-align:center}
.social{top:26px;width:100%;display:flex;justify-content:center;gap:14px}
.social span{width:30px;height:30px;border-radius:50%;background:var(--white)}
.copyright{top:76px;width:100%;font-size:11px}
</style>
</head>
<body>

<div class="topbar">
  <div class="abs contact">
    <span><svg width="11" height="11" viewBox="0 0 24 24"><path fill="#fff" d="M6.6 10.8a15 15 0 0 0 6.6 6.6l2.2-2.2a1 1 0 0 1 1-.25 11 11 0 0 0 3.6.6 1 1 0 0 1 1 1V20a1 1 0 0 1-1 1A17 17 0 0 1 3 4a1 1 0 0 1 1-1h3.5a1 1 0 0 1 1 1 11 11 0 0 0 .6 3.6 1 1 0 0 1-.25 1z"/></svg>+800-555-0199</span>
    <span><svg width="12" height="10" viewBox="0 0 24 18"><rect x="1" y="1" width="22" height="16" fill="none" stroke="#fff" stroke-width="2"/><path d="M1 1l11 9 11-9" fill="none" stroke="#fff" stroke-width="2"/></svg>hello@cedarsdevelopment.example</span>
  </div>
  <nav class="abs nav"><span>CONCEPT</span><span>CREATE</span><span>COMPLETE</span></nav>
</div>

<header class="site-header">
  <div class="abs brand"><span class="brand-name">CEDARS</span><span class="brand-sub">DEVELOPMENT CO.</span></div>
  <div class="abs menu-btn"><svg width="13" height="10" viewBox="0 0 13 10"><rect width="13" height="2" fill="#3d2a24"/><rect y="4" width="13" height="2" fill="#3d2a24"/><rect y="8" width="13" height="2" fill="#3d2a24"/></svg></div>
  <a class="abs btn btn-dark header-cta">Contact Us</a>
</header>

<section class="hero">
  <div class="abs hero-photo" role="img" aria-label="Man with glasses working on a laptop at a bright office desk"></div>
  <div class="abs hero-arrow"><svg width="10" height="12" viewBox="0 0 10 12"><path d="M7 1L2 6l5 5" fill="none" stroke="#444" stroke-width="2"/></svg></div>
  <div class="abs hero-rule"></div>
  <h1 class="abs hero-title">CEDARS DEVELOPMENT</h1>
  <p class="abs hero-sub">Brings your brand to life, online.</p>
  <a class="abs btn btn-dark hero-btn">Read More</a>
</section>

<section class="services">
  <p class="abs section-label">Concept. Create. Complete</p>
  <h2 class="abs section-title">What We Do</h2>
  <div class="abs service-card" style="left:172px"><h3>Design Happens Here</h3><p>We are leading the way in design innovation for modern websites. Clean, functional, intuitive websites for progressive businesses.</p></div>
  <div class="abs service-card" style="left:466px"><h3>Art Happens Here</h3><p>Building brands through design, we believe that contrast is everything. For industry leaders who set the pace and exceed expectations, we help give the company voice and soul.</p></div>
  <div class="abs service-card" style="left:757px"><h3>Ideas Happen Here</h3><p>Clients look to us for unique, exceptional solutions to their technology issues. We bring creativity to the table and solve your business' problems with actionable solutions.</p></div>
</section>

<section class="team">
  <p class="abs team-label">OUR CEDARS</p>
  <h2 class="abs team-title">CEDARS TEAM</h2>
  <p class="abs team-intro">Cedars Development Company focuses on creating extraordinary online experiences for extraordinary clients. We'll work with you to create the perfect online presence for your brand.</p>
  <article class="abs member" style="left:172px">
    <div class="member-photo" role="img" aria-label="Two colleagues reviewing work together at a desk" style="background:linear-gradient(90deg,#cfc7bd,#8a7a6c,#5b5049)"></div>
    <h3>Size Is Everything</h3>
    <p>We don't work in a massive corporate office and we don't have a mailroom. Not that there's anything wrong with that, it's just that we like knowing each other's names, and encourage our clients to know ours.</p>
    <a class="btn btn-light">Read More</a>
  </article>
  <article class="abs member" style="left:466px">
    <div class="member-photo" role="img" aria-label="Woman studying a monitor in a bright office" style="background:linear-gradient(90deg,#dfe6ee,#c6cfd8,#e8e2dc)"></div>
    <h3>Our Goal</h3>
    <p>Cedars Development brings your brand to life, online. We do it all when it comes to online commerce for retail stores, wholesalers and distributors. Taking your company online introduces a world of opportunity.</p>
    <a class="btn btn-light">Read More</a>
  </article>
  <article class="abs member" style="left:757px">
    <div class="member-photo" role="img" aria-label="Man on a phone call beside his laptop" style="background:linear-gradient(90deg,#eeeeea,#b9b2a8,#3a2f2a)"></div>
    <h3>Who's Owen?</h3>
    <p>Owen Marsh, owner of Cedars Development is not your typical principal. He's worked internationally with both Larkfield and Brightwater publications in photo production for titles including Modern Muse and Gilded Hour.</p>
    <a class="btn btn-light">Read More</a>
  </article>
</section>

<section class="approach">
  <p class="abs section-label">Cedars Development</p>
  <h2 class="abs section-title">We Get You</h2>
  <p class="abs approach-sub">Having a website isn't enough. You need to show your customers you understand the socially connected online world we live in.</p>
  <div class="abs approach-copy">
    <p>We help you create designs that capture the personality of your business and project the image you want your customers to see. Maybe you're a small company looking to sell yourself in the big leagues; maybe you're a big company that wants to look approachable; either way, we can make it happen.</p>
    <strong>You'll come across looking professional, unique and strikingly hip all at the same time.</strong>
  </div>
  <a class="abs btn btn-dark approach-btn">Read More</a>
  <div class="abs approach-photo" role="img" aria-label="Three business people reviewing documents together"></div>
</section>

<section class="contact">
  <p class="abs contact-kicker">GET IN TOUCH</p>
  <h2 class="abs contact-title">CONTACT US</h2>
  <div class="abs field field-name">Enter your name</div>
  <div class="abs field field-email">Enter your email id</div>
  <div class="abs field field-phone">Enter your phone number</div>
  <div class="abs field field-message">Message</div>
  <div class="abs submit">SUBMIT</div>
</section>

<footer class="site-footer">
  <div class="abs social" role="img" aria-label="Social network links"><span></span><span></span><span></span><span></span></div>
  <p class="abs copyright">© 2018 CEDARS DEVELOPMENT CO. ALL RIGHT RESERVED.</p>
</footer>

</body>
</html>
```